Mobile Oil Change company needs a flyer to promote new business

We need a flyer to 1) print & handout and 2) email out to potential customers. We are a mobile oil change company that comes to our customer locations to perform the work instead of customers going to traditional oil change companies. We have a 21 point inspection with our oil change. (21 point inspection details will not be on the flyer). Would like to keep the flyer simple but creative. I'm attaching 1) the write-up we created, 2) our logo (logo color is dark teal on white but other combinations are included if you wanted to propose a different color combination), and 3) additional services we offer. Logo font is Alegreya Sans.
Would like the additional services listed with icons and brief descriptions (similar to attachment) without pricing. Company website for reference is www.brookmerelubeworks.com.

Target Market(s)

Companies with many service vehicles such as Oil & Gas service companies, heating and air conditioning companies, utility companies, police departments, etc. Companies that prioritize convenience and maintenance first.

Font styles to use
Sans Serif

Colors
00a990

Requirements
Must have
• Simple but creative design with our logo at top of the flyer. Additional Services (details in document supplied) can be smaller and less prominent than other "main" content listed in the CONTENT document supplied.
Should not have
• Do not use animated character graphics in the flyer and limit (1) stock photos to A small area in the flyer.

```html
<!DOCTYPE html>
<html lang="en">
<head>
<meta charset="utf-8">
<title>Brookmere Lube Works – Mobile Oil Change Flyer</title>
<link href="https://fonts.googleapis.com/css2?family=Oswald:wght@600;700&family=Lato:wght@400;700;900&family=Montserrat:wght@800;900&display=swap" rel="stylesheet">
<style>
  :root {
    --teal: #00a990;
    --teal-dark: #008a76;
    --ink: #111111;
    --paper: #ffffff;
    --backdrop: #2e3546;
  }
  * { margin: 0; padding: 0; box-sizing: border-box; }
  html, body { width: 1200px; height: 1200px; overflow: hidden; background: var(--backdrop); }
  .flyer {
    position: absolute; left: 175px; top: 50px;
    width: 850px; height: 1100px;
    background: var(--paper); overflow: hidden;
    font-family: 'Lato', sans-serif; color: var(--ink);
  }
  .flyer-shapes { position: absolute; inset: 0; }
  .brand {
    position: absolute; left: 48px; top: 80px;
    display: flex; align-items: center; gap: 12px;
  }
  .brand-mark { width: 20px; height: 20px; background: var(--teal); }
  .brand-name {
    font-family: 'Lato', sans-serif; font-weight: 900; color: var(--teal);
    font-size: 30px; line-height: 1; letter-spacing: 1px; white-space: nowrap;
  }
  .brand-name small { display: block; font-size: 14px; letter-spacing: 5px; margin-top: 6px; }
  .headline {
    position: absolute; right: 36px; top: 24px; text-align: right; color: var(--ink);
  }
  .headline-main {
    font-family: 'Oswald', sans-serif; font-weight: 700; font-size: 82px;
    line-height: 0.95; letter-spacing: -1px; text-transform: uppercase; white-space: nowrap;
  }
  .headline-sub {
    font-family: 'Montserrat', sans-serif; font-weight: 900; font-size: 34px;
    line-height: 1.05; text-transform: uppercase; white-space: nowrap;
  }
  .headline-sub .accent { color: var(--paper); }
  .process { position: absolute; left: 50px; top: 478px; width: 540px; }
  .process-intro {
    color: var(--teal); font-weight: 900; font-size: 26px; line-height: 1.2; margin-bottom: 16px;
  }
  .process-steps { list-style: none; }
  .process-steps li {
    display: flex; align-items: center; gap: 10px;
    font-size: 16px; font-weight: 700; line-height: 1.2; margin-bottom: 10px; white-space: nowrap;
  }
  .step-drop { flex: none; width: 20px; height: 24px; }
  .benefits {
    position: absolute; left: 40px; top: 808px; width: 780px; list-style: none;
    color: var(--paper); font-weight: 900; font-size: 23px; line-height: 1.18;
  }
  .benefits li { display: flex; gap: 12px; margin-bottom: 6px; }
  .benefits svg { flex: none; width: 20px; height: 20px; margin-top: 4px; }
  .contact-call { position: absolute; left: 48px; top: 962px; }
  .call-title {
    font-family: 'Oswald', sans-serif; font-weight: 700; color: var(--teal);
    font-size: 60px; line-height: 1; text-transform: uppercase; letter-spacing: -0.5px; white-space: nowrap;
  }
  .contact-line {
    display: flex; align-items: center; gap: 10px;
    font-size: 19px; font-weight: 700; margin-top: 12px; white-space: nowrap;
  }
  .contact-line svg { width: 20px; height: 20px; flex: none; }
  .contact-phone { position: absolute; right: 36px; top: 962px; }
  .phone-number {
    display: flex; align-items: center; gap: 12px;
    font-family: 'Oswald', sans-serif; font-weight: 700; font-size: 50px; line-height: 1.2; white-space: nowrap;
  }
  .phone-number svg { width: 40px; height: 40px; flex: none; }
  .contact-phone .contact-line { margin-top: 4px; padding-left: 52px; }
</style>
</head>
<body>
<main class="flyer">
  <svg class="flyer-shapes" width="850" height="1100" viewBox="0 0 850 1100">
    <defs>
      <linearGradient id="oilTone" x1="0" y1="0" x2="1" y2="1">
        <stop offset="0" stop-color="#1f4f57"/>
        <stop offset="0.45" stop-color="#3a2a18"/>
        <stop offset="0.75" stop-color="#b8860b"/>
        <stop offset="1" stop-color="#2a1c10"/>
      </linearGradient>
      <linearGradient id="mechanicTone" x1="0" y1="0" x2="1" y2="1">
        <stop offset="0" stop-color="#d9dde2"/>
        <stop offset="0.5" stop-color="#6d7a8c"/>
        <stop offset="1" stop-color="#263a5c"/>
      </linearGradient>
    </defs>
    <polygon class="headline-band" points="330,0 850,0 850,215 440,215" fill="var(--teal)"/>
    <polygon role="img" aria-label="Photo: golden motor oil pouring from a bottle" points="440,215 850,215 850,780" fill="url(#oilTone)"/>
    <polygon role="img" aria-label="Photo: smiling mechanic working under an open car hood" points="40,200 420,200 595,450 40,450" fill="url(#mechanicTone)"/>
    <polygon class="benefits-band" points="0,800 850,768 850,935 0,935" fill="var(--teal)"/>
  </svg>

  <div class="brand">
    <span class="brand-mark"></span>
    <div class="brand-name">BROOKMERE<small>LUBE WORKS</small></div>
  </div>

  <header class="headline">
    <div class="headline-main">Hassle Free</div>
    <div class="headline-sub"><span class="accent">Oil changes on</span><br>your terms</div>
  </header>

  <section class="process">
    <p class="process-intro">Our simple 5-step process lets you schedule an appointment and get service to save time and money:</p>
    <ol class="process-steps">
      <li><svg class="step-drop" viewBox="0 0 20 24"><path d="M10 1C10 1 2 11 2 16a8 8 0 0 0 16 0C18 11 10 1 10 1z" fill="var(--teal)"/></svg>Call or email us to schedule service</li>
      <li><svg class="step-drop" viewBox="0 0 20 24"><path d="M10 1C10 1 2 11 2 16a8 8 0 0 0 16 0C18 11 10 1 10 1z" fill="var(--teal)"/></svg>Our highly trained technicians come to you for service</li>
      <li><svg class="step-drop" viewBox="0 0 20 24"><path d="M10 1C10 1 2 11 2 16a8 8 0 0 0 16 0C18 11 10 1 10 1z" fill="var(--teal)"/></svg>Service is performed quickly on your vehicle</li>
      <li><svg class="step-drop" viewBox="0 0 20 24"><path d="M10 1C10 1 2 11 2 16a8 8 0 0 0 16 0C18 11 10 1 10 1z" fill="var(--teal)"/></svg>Pay agreed-upon pricing and receipt is emailed to you</li>
      <li><svg class="step-drop" viewBox="0 0 20 24"><path d="M10 1C10 1 2 11 2 16a8 8 0 0 0 16 0C18 11 10 1 10 1z" fill="var(--teal)"/></svg>Services performed are tracked electronically and reminders created</li>
    </ol>
  </section>

  <ul class="benefits">
    <li><svg viewBox="0 0 20 20"><circle cx="10" cy="10" r="10" fill="#fff"/><path d="M5 10.5l3.2 3L15 7" stroke="var(--teal)" stroke-width="2.6" fill="none"/></svg>High quality synthetic oil used is best suited for commercial vehicles</li>
    <li><svg viewBox="0 0 20 20"><circle cx="10" cy="10" r="10" fill="#fff"/><path d="M5 10.5l3.2 3L15 7" stroke="var(--teal)" stroke-width="2.6" fill="none"/></svg>Service includes a 21-point inspection</li>
    <li><svg viewBox="0 0 20 20"><circle cx="10" cy="10" r="10" fill="#fff"/><path d="M5 10.5l3.2 3L15 7" stroke="var(--teal)" stroke-width="2.6" fill="none"/></svg>Additional services are available</li>
  </ul>

  <section class="contact-call">
    <div class="call-title">Call now at</div>
    <div class="contact-line">
      <svg viewBox="0 0 22 22"><rect x="1" y="4" width="20" height="14" fill="var(--teal)"/><path d="M1 4l10 8 10-8" stroke="#fff" stroke-width="1.6" fill="none"/></svg>
      Sales@BrookmereLubeWorks.com
    </div>
  </section>

  <section class="contact-phone">
    <div class="phone-number">
      <svg viewBox="0 0 24 24"><path d="M6.6 10.8a15.1 15.1 0 0 0 6.6 6.6l2.2-2.2a1 1 0 0 1 1-.25 11.4 11.4 0 0 0 3.6.57 1 1 0 0 1 1 1V20a1 1 0 0 1-1 1A17 17 0 0 1 3 4a1 1 0 0 1 1-1h3.5a1 1 0 0 1 1 1c0 1.250.2 2.45.57 3.57a1 1 0 0 1-.25 1z" fill="var(--teal)"/></svg>
      (833) 4-BLW-OIL
    </div>
    <div class="contact-line">
      <svg viewBox="0 0 22 22"><circle cx="11" cy="11" r="9" fill="none" stroke="var(--teal)" stroke-width="2"/><path d="M2 11h18M11 2c3 3 3 15 0 18M11 2c-3 3-3 15 0 18" stroke="var(--teal)" stroke-width="1.6" fill="none"/></svg>
      www.brookmerelubeworks.com
    </div>
  </section>
</main>
</body>
</html>
```